Torvane PT Business Card

I need the card to be bright/bold colours to stand out amongst others.
It needs to have my company logo.
I was not interested in pictures etc just a layout that attracts attention.

I have attached my old design which is very plain. I also needed change the contact details. And my description changed to Personal Trainer
Phone 0427309581
Facebook Torvane PT
No email address please, no street address.
And only Torvane PT (Please remove anything to do with Torvane Supplements)

```html
<!DOCTYPE html>
<html lang="en">
<head>
<meta charset="utf-8">
<title>Torvane PT Business Card</title>
<link rel="stylesheet" href="https://fonts.googleapis.com/css2?family=Open+Sans:wght@400;600;800&display=swap">
<style>
  :root {
    --backdrop: #2e3034;
    --brand-blue: #0a87cf;
    --card-white: #ffffff;
    --ink: #1e1e1e;
  }
  * { margin: 0; padding: 0; box-sizing: border-box; }
  html, body { width: 1200px; height: 864px; overflow: hidden; }
  body {
    background: var(--backdrop);
    font-family: "Open Sans", Arial, sans-serif;
    position: relative;
  }
  .card {
    position: absolute;
    width: 640px;
    height: 360px;
    border-radius: 3px;
    overflow: hidden;
  }
  .card--back { left: 200px; top: 50px; background: var(--brand-blue); }
  .card--front { left: 200px; top: 450px; background: var(--card-white); }
  .back-logo {
    position: absolute;
    left: 120px; top: 120px;
    width: 400px;
    text-align: center;
    color: var(--card-white);
  }
  .wordmark {
    font-weight: 800;
    letter-spacing: 2px;
    white-space: nowrap;
  }
  .back-logo .wordmark { font-size: 54px; line-height: 1; }
  .logo-rule { height: 2px; margin-top: 12px; }
  .back-logo .logo-rule { background: var(--card-white); }
  .front-logo {
    position: absolute;
    right: 50px; top: 50px;
    width: 380px;
    text-align: right;
  }
  .front-logo .wordmark { font-size: 50px; line-height: 1; color: var(--brand-blue); }
  .front-logo .logo-rule { background: var(--brand-blue); }
  .person { position: absolute; left: 60px; top: 168px; }
  .person__name {
    color: var(--brand-blue);
    font-weight: 600;
    font-size: 19px;
    letter-spacing: 0.5px;
  }
  .person__role { color: var(--ink); font-size: 14px; }
  .divider {
    position: absolute;
    left: 210px; right: 0; top: 222px;
    height: 2px;
    background: var(--brand-blue);
  }
  .contacts {
    position: absolute;
    right: 40px; top: 250px;
    list-style: none;
  }
  .contacts li {
    font-size: 15px;
    color: var(--ink);
    line-height: 28px;
    display: flex;
    justify-content: flex-end;
    align-items: center;
    gap: 8px;
  }
  .contacts .icon { width: 14px; height: 14px; flex: none; }
</style>
</head>
<body>
  <div class="card card--back">
    <div class="back-logo">
      <div class="wordmark">TORVANE PT</div>
      <div class="logo-rule"></div>
    </div>
  </div>

  <div class="card card--front">
    <div class="front-logo">
      <div class="wordmark">TORVANE PT</div>
      <div class="logo-rule"></div>
    </div>

    <div class="person">
      <div class="person__name">DANE MERCER</div>
      <div class="person__role">Personal Trainer</div>
    </div>

    <div class="divider"></div>

    <ul class="contacts">
      <li>0427309581
        <svg class="icon" viewBox="0 0 16 16" aria-hidden="true"><path fill="#0a87cf" d="M3.6 1.5l2.3 2.6-1.2 1.8c.9 2 2.4 3.5 4.4 4.4l1.8-1.2 2.6 2.3-1.3 2.3C7 13.3 2.7 9 1.3 2.8z"/></svg>
      </li>
      <li>Torvane PT
        <svg class="icon" viewBox="0 0 16 16" aria-hidden="true"><circle cx="8" cy="8" r="7" fill="#0a87cf"/></svg>
      </li>
    </ul>
  </div>
</body>
</html>
```